Lanworth's Finest magazine ad

This is a full page ad in a magazine announcing that I won The Top Picks Of Crelby Valley Realtor for 2023. The dimensions for the full page ad are 7.125" x 9.75"
I would like it to say "Thank You Crelby County for voting me Lanworth's Finest Realtor for 2022 & 2023!"

I am honored that the residents of this county have recognized my integrity, values, willingness to go above and beyond, to save my clients tons of money and stress, and to constantly pour back into this community.

If you are ever thinking about buying or selling a house, please don't hesitate to reach out, I am available 24/7 by text or phone call to save you money and provide the best top notch service:

Carlos Pendry
call/text 410-555-0147

Small at the bottom:
www.MaplePathHomes.com
2748 W Dorrance Ave, Ashcombe Falls 20904
833-555-0192

I am attaching my logo, the Lanworth's Finest 2023 logo, my picture, and last years ad (I'm hoping to make this years ad different and better)

```html
<!DOCTYPE html>
<html lang="en">
<head>
<meta charset="utf-8">
<title>Lanworth's Finest – Thank You Ad</title>
<link rel="stylesheet" href="https://fonts.googleapis.com/css2?family=Allura&family=Montserrat:wght@300;400;600;800&display=swap">
<style>
  :root {
    --backdrop: #3d3c3d;
    --paper: #ffffff;
    --navy: #1c3363;
    --orange: #ee7a2a;
    --ink: #1f2a44;
    --script-gray: #8f8f8f;
    --body-gray: #8a8a8a;
    --band-black: #050505;
    --badge: #2a2a2a;
  }
  html, body {
    margin: 0;
    width: 1200px;
    height: 1200px;
    overflow: hidden;
    background: var(--backdrop);
    font-family: "Montserrat", sans-serif;
  }
  .ad-page {
    position: absolute;
    left: 211px;
    top: 95px;
    width: 778px;
    height: 1010px;
    background: var(--paper);
    overflow: hidden;
  }
  .portrait {
    position: absolute;
    left: 380px;
    top: 68px;
    width: 398px;
    height: 942px;
    border-radius: 170px 0 0 0;
    background:
      linear-gradient(90deg, rgba(255,255,255,1) 0%, rgba(255,255,255,0) 25%),
      linear-gradient(180deg, #e2e2e2 0%, #9a9a9a 30%, #5e5e5e 70%, #474747 100%);
  }
  .brand {
    position: absolute;
    left: 287px;
    top: 42px;
    width: 200px;
    text-align: center;
    color: var(--navy);
  }
  .brand-mark {
    width: 64px;
    height: 64px;
    margin: 0 auto 16px;
    border-radius: 50%;
    background: var(--navy);
  }
  .brand-name {
    margin: 0;
    padding: 7px 0;
    font-weight: 600;
    font-size: 14px;
    letter-spacing: 0.5px;
    white-space: nowrap;
    border-top: 1px solid var(--navy);
    border-bottom: 1px solid var(--navy);
  }
  .brand-sub {
    margin-top: 4px;
    font-weight: 600;
    font-size: 7px;
    letter-spacing: 1.5px;
    white-space: nowrap;
  }
  .thanks {
    position: absolute;
    left: 52px;
    top: 206px;
    margin: 0;
    font-family: "Allura", cursive;
    font-weight: 400;
    font-size: 130px;
    line-height: 1;
    color: var(--script-gray);
    white-space: nowrap;
  }
  .headline {
    position: absolute;
    left: 53px;
    top: 350px;
    margin: 0;
    color: var(--ink);
    font-weight: 400;
    white-space: nowrap;
  }
  .headline span { display: block; }
  .headline .lead { font-size: 24px; line-height: 30px; }
  .headline .award {
    font-size: 34px;
    line-height: 44px;
    font-weight: 800;
    color: var(--orange);
    margin-top: 3px;
  }
  .headline .year { font-size: 24px; line-height: 30px; margin-top: 2px; }
  .badges {
    position: absolute;
    left: 86px;
    top: 477px;
    display: flex;
    gap: 27px;
  }
  .badge {
    width: 92px;
    height: 92px;
    border-radius: 50%;
    background: var(--badge);
  }
  .message {
    position: absolute;
    left: 53px;
    top: 586px;
    width: 305px;
    color: var(--body-gray);
    font-weight: 400;
    font-size: 12px;
    line-height: 18.4px;
  }
  .message p { margin: 0 0 18px; }
  .contact-band {
    position: absolute;
    left: 0;
    top: 801px;
    width: 778px;
    height: 81px;
    display: flex;
    color: #fff;
    font-size: 29px;
    font-weight: 400;
    white-space: nowrap;
  }
  .contact-band .phone {
    width: 488px;
    padding-left: 53px;
    box-sizing: border-box;
    background: linear-gradient(90deg, var(--navy) 88%, #10203f 100%);
    display: flex;
    align-items: center;
  }
  .contact-band .agent {
    flex: 1;
    background: var(--band-black);
    display: flex;
    align-items: center;
  }
  .details {
    position: absolute;
    left: 0;
    top: 887px;
    width: 490px;
    height: 102px;
    padding: 17px 0 0 53px;
    box-sizing: border-box;
    background: linear-gradient(90deg, #9b9b9b 0%, #b4b4b4 60%, #dcdcdc 100%);
    color: #fff;
    font-weight: 600;
    font-size: 13.5px;
    line-height: 24px;
    white-space: nowrap;
  }
  .details span { display: block; }
</style>
</head>
<body>
  <main class="ad-page">
    <div class="portrait" role="img" aria-label="Black and white portrait of the realtor in a blazer"></div>

    <header class="brand">
      <div class="brand-mark"></div>
      <p class="brand-name">THE MAPLE PATH TEAM</p>
      <div class="brand-sub">AT CRESTLINE REALTY</div>
    </header>

    <h1 class="thanks">Thank You</h1>

    <h2 class="headline">
      <span class="lead">Crelby County for voting me</span>
      <span class="award">LANWORTH'S FINEST</span>
      <span class="year">REALTOR for 2022 &amp; 2023!</span>
    </h2>

    <div class="badges">
      <div class="badge"></div>
      <div class="badge"></div>
    </div>

    <section class="message">
      <p>I am honored that the residents of this county have recognized my integrity, values, willingness to go above and beyond, to save my clients tons of money and stress, and to constantly pour back into this community.</p>
      <p>If you are ever thinking about buying or selling a house, please don't hesitate to reach out, I am available 24/7 by text or phone call to save you money and provide the best top notch service:</p>
    </section>

    <div class="contact-band">
      <div class="phone">call/text 410-555-0147</div>
      <div class="agent">Carlos Pendry</div>
    </div>

    <footer class="details">
      <span>www.MaplePathHomes.com</span>
      <span>2748 W Dorrance Ave, Ashcombe Falls 20904</span>
      <span>833-555-0192</span>
    </footer>
  </main>
</body>
</html>
```